I need a new business card design for my pharmacy.

I need a business card design. I will include my logo.
The card needs to be readable. I prefer to have my logo on one side along with my website, the other side includes the other information. Please use combination of black, neon green, white, and silver. This needs to catch the eye but yet be clearly visible and legible. Thanks

Industry/Entity Type

Pharmacy

Contact Information for Business Card

It needs to have the following information listed:
Mel's Apothecary Owner/Pharm D.
7134 North Brook Lane
Sioux Falls, SD 57231
Phone 605-318-6207
Fax 605-318-6209
email: mel@melsapothecary-example.com
www.melsapothecary-example.com
Store hours Monday-Friday 8 am- 7 pm
Saturday 8 am- 12 pm
Sunday Closed
Please utilize the colors black, white, and neon green, maybe silver.

Requirements
Must have
• It needs to be easily readable!
Nice to have
• It should catch the eye.
Should not have
• Do not use any other colors except listed: black, neon green, white, & silver.

```html
<!DOCTYPE html>
<html lang="en">
<head>
<meta charset="utf-8">
<title>Mel's Apothecary — Business Card</title>
<link rel="stylesheet" href="https://fonts.googleapis.com/css2?family=Source+Sans+3:wght@600;700&family=Arimo:wght@400;700&display=swap">
<style>
  :root {
    --neon-green: #8cc63f;
    --ink: #141414;
    --paper: #ffffff;
    --paper-soft: #f4f4f4;
    --silver: #c9c9c9;
    --backdrop: #e6e6e6;
    --display: "Source Sans 3", sans-serif;
    --body: "Arimo", sans-serif;
  }
  * { box-sizing: border-box; margin: 0; padding: 0; }
  html, body { width: 1200px; height: 902px; overflow: hidden; }
  body {
    background: var(--backdrop);
    display: flex;
    flex-direction: column;
    align-items: center;
    justify-content: center;
    gap: 40px;
  }
  .card {
    position: relative;
    width: 700px;
    height: 400px;
    overflow: hidden;
    border-radius: 4px;
    box-shadow: 0 6px 18px rgba(0,0,0,.18);
  }

  /* Front */
  .card--front { background: var(--paper-soft); }
  .card__wave { position: absolute; inset: 0; width: 100%; height: 100%; }
  .brand-mark {
    position: absolute; left: 128px; top: 118px;
    width: 52px; height: 52px; border-radius: 50%;
    background: var(--neon-green);
  }
  .brand-divider {
    position: absolute; left: 228px; top: 58px;
    width: 2px; height: 124px; background: var(--ink);
  }
  .brand-name {
    position: absolute; left: 250px; top: 44px;
    font-family: var(--display); font-weight: 700;
    font-size: 46px; line-height: 1.1; letter-spacing: -0.5px;
    color: var(--ink); white-space: nowrap;
  }
  .holder {
    position: absolute; left: 56px; top: 322px;
    font-family: var(--body);
  }
  .holder__name { font-weight: 700; font-size: 22px; color: var(--paper); }
  .holder__title { font-size: 18px; color: var(--silver); margin-top: 4px; }
  .contact-divider {
    position: absolute; left: 362px; top: 250px;
    width: 1px; height: 128px; background: var(--silver);
  }
  .contact-list {
    position: absolute; left: 386px; top: 222px;
    list-style: none; font-family: var(--body);
    font-size: 15px; color: var(--paper);
  }
  .contact-list li {
    display: flex; align-items: center; gap: 10px;
    height: 26px; white-space: nowrap;
  }
  .contact-list svg { width: 14px; height: 14px; flex: none; }
  .contact-list .indent { padding-left: 24px; }

  /* Back */
  .card--back {
    background: var(--neon-green);
    display: flex; flex-direction: column;
    align-items: center; justify-content: center;
    gap: 48px;
  }
  .back-brand { display: flex; align-items: center; gap: 18px; }
  .back-brand__mark {
    width: 62px; height: 62px; border-radius: 50%; background: var(--ink);
  }
  .back-brand__name {
    font-family: var(--display); font-weight: 700;
    font-size: 58px; color: var(--ink); letter-spacing: -0.5px;
  }
  .store-hours {
    font-family: var(--body); font-weight: 700;
    font-size: 20px; line-height: 1.45;
    color: var(--ink); text-align: center;
  }
</style>
</head>
<body>

  <section class="card card--front" aria-label="Card front">
    <svg class="card__wave" viewBox="0 0 700 400" preserveAspectRatio="none" aria-hidden="true">
      <path fill="#8cc63f" d="M0,280 C200,280 260,262 330,220 C400,178 480,150 700,145 L700,400 L0,400 Z"/>
      <path fill="#141414" d="M0,296 C200,296 270,278 340,236 C410,194 490,166 700,161 L700,400 L0,400 Z"/>
    </svg>

    <div class="brand-mark"></div>
    <div class="brand-divider"></div>
    <h1 class="brand-name">Mel's Apothecary</h1>

    <div class="holder">
      <p class="holder__name">Mel's Apothecary</p>
      <p class="holder__title">Owner/Pharm D.</p>
    </div>

    <div class="contact-divider"></div>
    <ul class="contact-list">
      <li>
        <svg viewBox="0 0 14 14" aria-label="Phone"><path fill="#fff" d="M3 1l2.5 0 1 3-1.6 1.2a7 7 0 0 0 3.9 3.9L10 7.5l3 1V11a2 2 0 0 1-2 2A10 10 0 0 1 1 3a2 2 0 0 1 2-2z"/></svg>
        605-318-6207
      </li>
      <li>
        <svg viewBox="0 0 14 14" aria-label="Fax"><rect x="3" y="1" width="8" height="4" fill="#fff"/><rect x="1" y="5" width="12" height="6" rx="1" fill="#fff"/><rect x="3" y="9" width="8" height="4" fill="#fff" stroke="#141414"/></svg>
        605-318-6209
      </li>
      <li>
        <svg viewBox="0 0 14 14" aria-label="Email"><rect x="1" y="3" width="12" height="8" fill="#fff"/><path d="M1 3l6 5 6-5" fill="none" stroke="#141414" stroke-width="1.2"/></svg>
        mel@melsapothecary-example.com
      </li>
      <li>
        <svg viewBox="0 0 14 14" aria-label="Website"><circle cx="7" cy="7" r="5.8" fill="none" stroke="#fff" stroke-width="1.4"/><ellipse cx="7" cy="7" rx="2.4" ry="5.8" fill="none" stroke="#fff" stroke-width="1"/><path d="M1.2 7h11.6" stroke="#fff" stroke-width="1"/></svg>
        www.melsapothecary-example.com
      </li>
      <li>
        <svg viewBox="0 0 14 14" aria-label="Address"><path fill="#fff" d="M7 1a4.5 4.5 0 0 1 4.5 4.5C11.5 9 7 13 7 13S2.5 9 2.5 5.5A4.5 4.5 0 0 1 7 1z"/><circle cx="7" cy="5.5" r="1.6" fill="#141414"/></svg>
        7134 North Brook Lane
      </li>
      <li class="indent">Sioux Falls, SD 57231</li>
    </ul>
  </section>

  <section class="card card--back" aria-label="Card back">
    <div class="back-brand">
      <div class="back-brand__mark"></div>
      <p class="back-brand__name">Mel's Apothecary</p>
    </div>
    <p class="store-hours">
      Store hours Monday-Friday 8 am - 7 pm<br>
      Saturday 8 am - 12 pm &nbsp;·&nbsp; Sunday Closed
    </p>
  </section>

</body>
</html>
```